Hi! We require a design for business cards for directors and head teachers of an international daycare for children 0 - 9. We are family-owned, -operated and -oriented. We have six locations, looking to franchise. Our USPs are: 1) Flexibility 2) Quality teachers 3) International culture 4) Best nutrition We are quality teachers and professional caretakers, but with creativity and personality! Business cards should be playful (but no Comic Sans or baby hand prints), colorful (but no rainbows), and have some breathing space. It should be obvious from the business card that we're a daycare. In 2020 we'll be launching our new website based on this design: https://plomvane.io/47K2RQLWZTD The font in the new website will be Houschka (medium, demibold, bold). We will keep our current logo, included in the files here. There are also screenshots of some designs we like. Show us your best! :)

Industry/Entity Type

Childcare

Contact Information for Business Card

Lotte de Vries-Bakhuis
Communications Wizard
Poppel Hoek International Daycare
Kastanjeweg 47 B, 2316 KR Leiden
www.poppelhoek.nl
+31 647315082

Font styles to use
Serif
Sans Serif

Colors

Designer to choose colors to be used in the design.

Requirements
Must have
• Color

```html
<!DOCTYPE html>
<html lang="en">
<head>
<meta charset="utf-8">
<title>Poppel Hoek – Business Card</title>
<link rel="stylesheet" href="https://fonts.googleapis.com/css2?family=Fredoka:wght@500;600&family=Roboto:wght@400&display=swap">
<style>
  :root {
    --backdrop: #bdbdbd;
    --card: #f7f7f7;
    --pink: #d94d8a;
    --blue: #2ea1d8;
    --ink: #2f2f2f;
    --pattern-a: #fbe7f0;
    --pattern-b: #e3f2fb;
  }
  * { margin: 0; padding: 0; box-sizing: border-box; }
  html, body { width: 1200px; height: 576px; overflow: hidden; }
  body { background: var(--backdrop); position: relative; font-family: "Roboto", sans-serif; }

  .card {
    position: absolute;
    top: 138px;
    width: 483px;
    height: 293px;
    background: var(--card);
    border-radius: 9px;
    overflow: hidden;
  }
  .card--front { left: 82px; }
  .card--back { left: 602px; }

  .doodle-pattern {
    position: absolute; inset: 0;
    background: linear-gradient(135deg, var(--pattern-a), var(--card) 45%, var(--pattern-b));
  }
  .brand-name {
    position: absolute;
    font-family: "Fredoka", sans-serif;
    font-weight: 600;
    color: var(--pink);
    line-height: 0.95;
    text-align: center;
  }
  .card--front .brand-name {
    left: 0; right: 0; top: 100px;
    font-size: 50px;
  }
  .card--back .brand-name {
    left: 26px; top: 82px; width: 200px;
    font-size: 38px;
  }

  .waves { position: absolute; left: 0; top: 0; width: 483px; height: 293px; }

  .person {
    position: absolute; right: 26px; top: 44px; text-align: right;
  }
  .person__name {
    font-family: "Fredoka", sans-serif; font-weight: 500;
    font-size: 18px; color: var(--pink);
  }
  .person__role { font-size: 12px; color: var(--ink); margin-top: 4px; }

  .contact {
    position: absolute; right: 26px; top: 192px;
    list-style: none; text-align: right; color: #fff; font-size: 12px;
  }
  .contact li { display: flex; justify-content: flex-end; align-items: center; gap: 5px; height: 18px; }
  .contact .contact__address { margin-top: 7px; }
  .contact svg { width: 10px; height: 10px; fill: #fff; }
</style>
</head>
<body>

<section class="card card--front">
  <div class="doodle-pattern" role="img" aria-label="Playful pink, blue and grey line doodles of toys, stars, rockets and houses"></div>
  <div class="brand-name">Poppel<br>Hoek</div>
</section>

<section class="card card--back">
  <svg class="waves" viewBox="0 0 483 293" aria-hidden="true">
    <path d="M0 256 C120 310 230 170 483 140 L483 293 L0 293 Z" fill="var(--blue)"/>
    <path d="M0 222 C120 290 230 150 483 118 L483 132 C230 164 120 300 0 236 Z" fill="var(--pink)"/>
    <path d="M0 262 C60 290 150 290 240 262 C150 280 60 282 0 256 Z" fill="var(--pink)"/>
  </svg>

  <div class="brand-name">Poppel<br>Hoek</div>

  <div class="person">
    <p class="person__name">Lotte de Vries-Bakhuis</p>
    <p class="person__role">Communications Wizard</p>
  </div>

  <ul class="contact">
    <li>+31 647315082
      <svg viewBox="0 0 10 10"><path d="M1 3 Q1 1 5 1 Q9 1 9 3 L7 4 L6 3 L4 3 L3 4 Z M2 5 L8 5 L9 9 L1 9 Z"/></svg></li>
    <li>lotte@poppelhoek.nl
      <svg viewBox="0 0 10 10"><path d="M0 2 H10 V8 H0 Z M0.8 2.6 L5 5.6 L9.2 2.6 V3.4 L5 6.4 L0.8 3.4 Z" fill-rule="evenodd"/></svg></li>
    <li>www.poppelhoek.nl
      <svg viewBox="0 0 10 10"><circle cx="5" cy="5" r="4.5"/></svg></li>
    <li class="contact__address">Kastanjeweg 47 B, 2316 KR Leiden</li>
  </ul>
</section>

</body>
</html>
```